Association Insurance WhitePaper

Need white paper layout design for cover page, data pages and back page, much like a powerpoint design. Looking for similar designs as the uploaded drawing style.

```html
<!DOCTYPE html>
<html lang="en">
<head>
<meta charset="UTF-8">
<title>Association Insurance White Paper – Slide Set</title>
<link rel="stylesheet" href="https://fonts.googleapis.com/css2?family=Questrial&family=Arimo:wght@400;700&family=Montserrat:wght@500;600;700&display=swap">
<style>
  :root {
    --page-bg: #c9cacc;
    --slide-bg: #ffffff;
    --ink: #3a3a3c;
    --ink-soft: #6b6c70;
    --panel: #dcdcdd;
    --swot-s: #76777b;
    --swot-w: #8b8c90;
    --swot-o: #a3a4a8;
    --swot-t: #b9babe;
    --sky-pale: #e4f3fa;
    --sky-lilac: #dcd6f2;
    --city-tone: #b4bbdb;
    --city-deep: #8e96c2;
    --faint-city: #eceded;
  }
  * { box-sizing: border-box; margin: 0; padding: 0; }
  html, body { width: 1200px; height: 2540px; overflow: hidden; }
  body {
    background: var(--page-bg);
    font-family: "Arimo", Arial, sans-serif;
    color: var(--ink);
    position: relative;
  }
  .slide {
    position: absolute;
    left: 118px;
    width: 972px;
    height: 547px;
    background: var(--slide-bg);
    overflow: hidden;
    box-shadow: 0 3px 8px rgba(0,0,0,0.18);
  }
  .slide--cover { top: 108px; }
  .slide--agenda { top: 697px; }
  .slide--swot { top: 1288px; }
  .slide--closing { top: 1877px; }

  .abs { position: absolute; }

  /* Sketched skyline artwork area */
  .skyline-art {
    background: linear-gradient(to bottom, var(--sky-pale) 0%, var(--sky-lilac) 35%, var(--city-tone) 65%, var(--city-deep) 100%);
    -webkit-mask-image: linear-gradient(to bottom, transparent 0%, #000 30%);
            mask-image: linear-gradient(to bottom, transparent 0%, #000 30%);
  }
  .cover-art { left: 0; top: 140px; width: 972px; height: 407px; }
  .closing-art {
    left: 96px; top: 78px; width: 800px; height: 352px;
    -webkit-mask-image: linear-gradient(to bottom, transparent 0%, #000 30%, #000 88%, transparent 100%);
            mask-image: linear-gradient(to bottom, transparent 0%, #000 30%, #000 88%, transparent 100%);
  }

  /* Cover */
  .cover-title {
    right: 45px; top: 56px;
    text-align: right;
    font-family: "Questrial", sans-serif;
    font-size: 29px;
    line-height: 39px;
    letter-spacing: 1.6px;
    text-transform: uppercase;
    color: var(--ink);
  }

  /* Faint skyline backdrop */
  .faint-city {
    left: 0; top: 290px; width: 840px; height: 257px;
    background: var(--faint-city);
    -webkit-mask-image:
      linear-gradient(to bottom, transparent 0%, #000 45%),
      linear-gradient(to right, #000 75%, transparent 100%);
    -webkit-mask-composite: source-in;
            mask-image:
      linear-gradient(to bottom, transparent 0%, #000 45%),
      linear-gradient(to right, #000 75%, transparent 100%);
            mask-composite: intersect;
  }
  .slide--swot .faint-city { top: 250px; height: 297px; }

  .section-title {
    font-family: "Questrial", sans-serif;
    font-size: 28px;
    letter-spacing: 1px;
    color: var(--ink);
    line-height: 35px;
  }
  .body-copy {
    font-size: 12.5px;
    line-height: 19px;
    color: var(--ink-soft);
  }

  /* Agenda */
  .toc-title { left: 90px; top: 222px; }
  .toc-copy { left: 92px; top: 270px; width: 375px; }
  .agenda-panel {
    left: 528px; top: 98px; width: 361px; height: 361px;
    background: var(--panel);
    border-radius: 30px;
  }
  .agenda-pill {
    left: 507px; top: 136px; width: 158px; height: 42px;
    background: #f3f3f3;
    border-radius: 21px;
  }
  .agenda-pill__icon {
    position: absolute; left: 0; top: 0;
    width: 42px; height: 42px; border-radius: 50%;
    background: var(--swot-s);
  }
  .agenda-pill__label {
    position: absolute; left: 54px; top: 11px;
    font-family: "Montserrat", sans-serif; font-weight: 600;
    font-size: 17px; letter-spacing: 1.5px; color: var(--ink);
  }
  .agenda-year {
    left: 748px; top: 149px; width: 78px; text-align: center;
    font-family: "Montserrat", sans-serif; font-weight: 500;
    font-size: 18px; color: var(--ink);
  }
  .agenda-year::after {
    content: ""; position: absolute; left: 0; right: 0; bottom: -5px;
    border-top: 1px solid var(--ink-soft);
  }
  .agenda-item { left: 570px; width: 290px; height: 24px; }
  .agenda-item__dot {
    position: absolute; left: 0; top: 4px; width: 5px; height: 5px;
    border-radius: 50%; background: var(--ink-soft);
  }
  .agenda-item__text {
    position: absolute; left: 14px; top: -1px;
    font-size: 11px; color: var(--ink-soft);
  }
  .agenda-item__rule {
    position: absolute; left: 14px; top: 14px; width: 240px;
    border-top: 1px solid #9fa0a3;
  }
  .agenda-item__num {
    position: absolute; left: 263px; top: 4px;
    width: 20px; height: 20px; border-radius: 50%;
    background: #fff; text-align: center;
    font-size: 9px; font-weight: 700; line-height: 20px; color: var(--ink-soft);
  }

  /* SWOT */
  .intro-title { left: 60px; top: 76px; }
  .intro-copy { left: 62px; top: 170px; width: 440px; text-align: justify; font-size: 12.5px; line-height: 21px; }
  .feature { left: 110px; width: 360px; }
  .feature__icon { position: absolute; left: 0; top: 0; }
  .feature__title {
    position: absolute; left: 67px; top: 0;
    font-family: "Montserrat", sans-serif; font-weight: 500;
    font-size: 14.5px; letter-spacing: 1.2px; color: var(--ink);
  }
  .feature__copy { position: absolute; left: 67px; top: 26px; width: 290px; font-size: 12.5px; line-height: 17px; }
  .swot-column {
    left: 532px; top: 58px; width: 94px; height: 432px;
    border-radius: 14px; overflow: hidden;
  }
  .swot-cell {
    height: 108px; display: flex; align-items: center; justify-content: center;
    font-family: "Montserrat", sans-serif; font-weight: 700;
    font-size: 38px; color: #fff;
  }
  .swot-cell--s { background: var(--swot-s); }
  .swot-cell--w { background: var(--swot-w); }
  .swot-cell--o { background: var(--swot-o); }
  .swot-cell--t { background: var(--swot-t); }
  .swot-note { left: 665px; width: 250px; }
  .swot-note__title {
    font-family: "Montserrat", sans-serif; font-weight: 600;
    font-size: 14.5px; letter-spacing: 1.3px; color: var(--ink); margin-bottom: 4px;
  }
  .swot-note .body-copy { font-size: 12px; line-height: 16px; }

  /* Closing */
  .closing-title {
    left: 0; width: 980px; top: 410px; text-align: center;
    font-family: "Questrial", sans-serif;
    font-size: 47px; letter-spacing: 3px; color: var(--ink);
  }
</style>
</head>
<body>

<section class="slide slide--cover">
  <h1 class="abs cover-title">7 Ways to Help Generate<br>Income Once Your Portfolio<br>Reaches $1,000,000</h1>
  <div class="abs skyline-art cover-art" role="img" aria-label="Hand-sketched city skyline with pastel blue, lilac and yellow clouds"></div>
</section>

<section class="slide slide--agenda">
  <div class="abs faint-city" role="img" aria-label="Faint sketched city skyline backdrop"></div>
  <h2 class="abs section-title toc-title">Table Of Content</h2>
  <p class="abs body-copy toc-copy">Lorem Ipsum is simply dummy text of the printing and typesetting industry. Lorem Ipsum has been the industry's standard dummy text ever since the 1500s,</p>

  <div class="abs agenda-panel"></div>
  <div class="abs agenda-pill">
    <span class="agenda-pill__icon">
      <svg width="42" height="42" viewBox="0 0 42 42" aria-hidden="true">
        <g fill="#fff">
          <circle cx="14" cy="15" r="1.4"/><rect x="17" y="14" width="12" height="2" rx="1"/>
          <circle cx="14" cy="21" r="1.4"/><rect x="17" y="20" width="12" height="2" rx="1"/>
          <circle cx="14" cy="27" r="1.4"/><rect x="17" y="26" width="12" height="2" rx="1"/>
        </g>
      </svg>
    </span>
    <span class="agenda-pill__label">AGENDA</span>
  </div>
  <div class="abs agenda-year">2050</div>

  <div class="abs agenda-item" style="top:210px"><span class="agenda-item__dot"></span><span class="agenda-item__text">Simple Text One</span><span class="agenda-item__rule"></span><span class="agenda-item__num">02</span></div>
  <div class="abs agenda-item" style="top:251px"><span class="agenda-item__dot"></span><span class="agenda-item__text">Simple Text Two</span><span class="agenda-item__rule"></span><span class="agenda-item__num">04</span></div>
  <div class="abs agenda-item" style="top:293px"><span class="agenda-item__dot"></span><span class="agenda-item__text">Simple Text Three</span><span class="agenda-item__rule"></span><span class="agenda-item__num">06</span></div>
  <div class="abs agenda-item" style="top:334px"><span class="agenda-item__dot"></span><span class="agenda-item__text">Simple Text Four</span><span class="agenda-item__rule"></span><span class="agenda-item__num">08</span></div>
  <div class="abs agenda-item" style="top:376px"><span class="agenda-item__dot"></span><span class="agenda-item__text">Simple Text Five</span><span class="agenda-item__rule"></span><span class="agenda-item__num">10</span></div>
  <div class="abs agenda-item" style="top:417px"><span class="agenda-item__dot"></span><span class="agenda-item__text">Simple Text Six</span><span class="agenda-item__num">12</span></div>
</section>

<section class="slide slide--swot">
  <div class="abs faint-city" role="img" aria-label="Faint sketched city skyline backdrop"></div>
  <h2 class="abs section-title intro-title">Text<br>Added Here</h2>
  <p class="abs body-copy intro-copy">Lorem Ipsum is simply dummy text of the printing and typesetting industry. Lorem Ipsum has been the industry's standard dummy text ever since the 1500s, when an unknown printer took a galley of type and scrambled it to make a type specimen book.</p>

  <div class="abs feature" style="top:283px">
    <svg class="feature__icon" width="46" height="42" viewBox="0 0 46 42" aria-hidden="true">
      <g fill="none" stroke="#3a3a3c" stroke-width="3" stroke-linejoin="round">
        <rect x="3" y="3" width="40" height="26" rx="4"/>
        <line x1="3" y1="22" x2="43" y2="22"/>
        <line x1="23" y1="29" x2="23" y2="37"/>
        <line x1="13" y1="38" x2="33" y2="38" stroke-linecap="round"/>
      </g>
    </svg>
    <div class="feature__title">SIMPLE TEXT HERE</div>
    <p class="feature__copy body-copy">Lorem Ipsum is simply dummy text of the printing and typesetting industry.</p>
  </div>
  <div class="abs feature" style="top:390px">
    <svg class="feature__icon" width="46" height="44" viewBox="0 0 46 44" aria-hidden="true">
      <g fill="none" stroke="#3a3a3c" stroke-width="3" stroke-linecap="round">
        <polyline points="3,2 3,41 44,41"/>
        <line x1="12" y1="34" x2="12" y2="24"/>
        <line x1="19" y1="34" x2="19" y2="16"/>
        <line x1="26" y1="34" x2="26" y2="22"/>
        <line x1="33" y1="34" x2="33" y2="12"/>
      </g>
    </svg>
    <div class="feature__title">SIMPLE TEXT HERE</div>
    <p class="feature__copy body-copy">Lorem Ipsum is simply dummy text of the printing and typesetting industry.</p>
  </div>

  <div class="abs swot-column">
    <div class="swot-cell swot-cell--s">S</div>
    <div class="swot-cell swot-cell--w">W</div>
    <div class="swot-cell swot-cell--o">O</div>
    <div class="swot-cell swot-cell--t">T</div>
  </div>

  <div class="abs swot-note" style="top:85px"><div class="swot-note__title">LOREM IPSUM</div><p class="body-copy">Lorem Ipsum is simply dummy text of the printing and typesetting industry.</p></div>
  <div class="abs swot-note" style="top:191px"><div class="swot-note__title">LOREM IPSUM</div><p class="body-copy">Lorem Ipsum is simply dummy text of the printing and typesetting industry.</p></div>
  <div class="abs swot-note" style="top:296px"><div class="swot-note__title">LOREM IPSUM</div><p class="body-copy">Lorem Ipsum is simply dummy text of the printing and typesetting industry.</p></div>
  <div class="abs swot-note" style="top:406px"><div class="swot-note__title">LOREM IPSUM</div><p class="body-copy">Lorem Ipsum is simply dummy text of the printing and typesetting industry.</p></div>
</section>

<section class="slide slide--closing">
  <div class="abs skyline-art closing-art" role="img" aria-label="Hand-sketched city skyline with pastel clouds above a waterline"></div>
  <div class="abs closing-title">THANK YOU</div>
</section>

</body>
</html>
```